Business Card Design for Cybersecurity Company - Quorvent Systems

We need a business card design for our new cybersecurity company, Quorvent. We’re going for a clean, hi tech look that feels modern, premium, and trustworthy. We want a design that really stands out and makes people say WOW when we hand it over!

Quorvent delivers reliable IT support and managed services for small and mid sized businesses. We help companies stay secure, efficient, and connected through proactive monitoring, cybersecurity services, cloud management, and remote support.

Target Market(s)

Designers should target small and mid sized businesses that need dependable cybersecurity and IT support.

Industry/Entity Type

Cybersecurity, Managed Service Provider, IT services

Contact Information for Business Card

Contact information

Requirements
Must have
• The card should look clean, modern, and tech focused, with the Quorvent logo, clear contact info, and strong readability. It needs to feel premium and professional while still keeping a simple layout that fits a cybersecurity and IT brand.
Nice to have
• Nice to have elements include subtle touches that give the card a modern, tech feel, along with a layout that works well in different background styles.
Should not have
• The card should avoid clutter, loud graphics, or anything that takes attention away from the logo and contact details.

```html
<!DOCTYPE html>
<html lang="en">
<head>
<meta charset="utf-8">
<title>Quorvent Systems – Business Card</title>
<link rel="stylesheet" href="https://fonts.googleapis.com/css2?family=Ubuntu:wght@500;700&family=Noto+Sans:wght@400&display=swap">
<style>
  :root {
    --bg: #adadad;
    --card-white: #ffffff;
    --brand-blue: #3a5cf5;
    --brand-purple: #6a2bd9;
    --brand-mid: #4a3ee8;
    --ink: #1d1d22;
    --back-start: #3764f6;
    --back-end: #7322d8;
    --white: #ffffff;
  }
  * { box-sizing: border-box; margin: 0; padding: 0; }
  html, body { width: 1093px; height: 1200px; overflow: hidden; }
  body {
    background: var(--bg);
    position: relative;
    font-family: "Noto Sans", Arial, sans-serif;
    color: var(--ink);
  }
  .card {
    position: absolute;
    left: 264px;
    width: 580px;
    height: 356px;
    border-radius: 26px;
    overflow: hidden;
  }
  .card--front { top: 226px; background: var(--card-white); }
  .card--back {
    top: 621px;
    background: linear-gradient(30deg, var(--back-start) 0%, #4a4fec 50%, var(--back-end) 100%);
  }

  .brand {
    position: absolute;
    display: flex;
    align-items: center;
    gap: 12px;
    font-family: "Ubuntu", Arial, sans-serif;
    font-weight: 500;
    white-space: nowrap;
  }
  .brand__dot { border-radius: 50%; flex: none; }
  .card--front .brand { left: 280px; top: 70px; color: var(--brand-mid); font-size: 27px; }
  .card--front .brand__dot { width: 40px; height: 40px; background: var(--brand-mid); }
  .card--back .brand { left: 50%; top: 50%; transform: translate(-50%, -50%); color: var(--white); font-size: 38px; }
  .card--back .brand__dot { width: 56px; height: 56px; background: var(--white); }

  .accent-bar {
    position: absolute; left: 0; top: 220px; width: 15px; height: 44px;
    background: linear-gradient(180deg, var(--brand-purple), var(--brand-blue));
  }
  .holder__name {
    position: absolute; left: 29px; top: 214px;
    font-family: "Ubuntu", Arial, sans-serif; font-weight: 700; font-size: 26px;
    background: linear-gradient(90deg, var(--brand-blue), var(--brand-purple));
    -webkit-background-clip: text; background-clip: text; color: transparent;
  }
  .holder__title { position: absolute; left: 29px; top: 243px; font-size: 16px; }
  .divider {
    position: absolute; left: 29px; top: 269px; width: 514px; height: 1.5px;
    background: var(--brand-blue);
  }
  .contact { position: absolute; top: 283px; list-style: none; font-size: 16.5px; }
  .contact--left { left: 29px; }
  .contact--right { left: 205px; }
  .contact li { display: flex; align-items: center; gap: 8px; height: 21px; }
  .contact svg { width: 15px; height: 15px; flex: none; fill: none; stroke: var(--brand-mid); stroke-width: 1.8; }
  .contact .accent { color: var(--brand-mid); }
</style>
</head>
<body>
  <section class="card card--front" aria-label="Card front">
    <div class="brand"><span class="brand__dot"></span>Quorvent Systems</div>
    <span class="accent-bar"></span>
    <h1 class="holder__name">Dana Whitlock</h1>
    <p class="holder__title">Owner | CEO | Quorvent Systems</p>
    <span class="divider"></span>
    <ul class="contact contact--left">
      <li><svg viewBox="0 0 24 24"><path d="M5 3h4l2 5-2.5 1.5a11 11 0 0 0 6 6L16 13l5 2v4a2 2 0 0 1-2 2A17 17 0 0 1 3 5a2 2 0 0 1 2-2z"/></svg>(855) 482-7710</li>
      <li><svg viewBox="0 0 24 24"><rect x="6" y="2" width="12" height="20" rx="2"/><line x1="11" y1="18" x2="13" y2="18"/></svg>(813) 555-0192</li>
    </ul>
    <ul class="contact contact--right">
      <li><svg viewBox="0 0 24 24"><rect x="2" y="5" width="20" height="14"/><path d="M2 5l10 8 10-8"/></svg>dana@quorventsys.com</li>
      <li><svg viewBox="0 0 24 24"><circle cx="12" cy="12" r="10"/><ellipse cx="12" cy="12" rx="4" ry="10"/><line x1="2" y1="12" x2="22" y2="12"/></svg><span>www.<span class="accent">quorventsys</span>.com</span></li>
    </ul>
  </section>

  <section class="card card--back" aria-label="Card back">
    <div class="brand"><span class="brand__dot"></span>Quorvent Systems</div>
  </section>
</body>
</html>
```